FC Morlan - Creation of a AD banner for our yearly event

We are a local soccer club in Switzerland. We're organizing a event that will substitute to our yearly club dinner. We need a banner AD to promote on the social networks this event.
We would like to see design that use one or the 2 colors of the club (blue and red).
This Ad should link to a online shop where we can buy vouchers.

Requirements
Must have
• Logo of the club
Title : Fête des lanternes d'hiver
Call to action : Plus d'informations
Side texte : Grande Tombola
Banner size : W300xH250 or W300xH600
Nice to have
• Promotion texte: Soutenez le FC Morlan et les restaurateurs locaux

```html
<!DOCTYPE html>
<html lang="fr">
<head>
<meta charset="utf-8">
<title>FC Morlan – Fête des lanternes d'hiver</title>
<link href="https://fonts.googleapis.com/css2?family=Barlow+Condensed:ital,wght@0,700;1,700;1,800&family=Archivo:wght@600;700&display=swap" rel="stylesheet">
<style>
  :root {
    --stage: #000000;
    --paper: #ffffff;
    --ink: #111111;
    --navy: #10233a;
    --club-blue: #1b86cf;
    --club-red: #e1253a;
    --player-dark: #2a0d12;
  }
  * { margin: 0; padding: 0; box-sizing: border-box; }
  html, body { width: 1200px; height: 675px; overflow: hidden; background: var(--stage); }
  .banner {
    position: absolute; left: 296px; top: 84px;
    width: 608px; height: 505px;
    background: var(--paper); overflow: hidden;
  }
  .title {
    position: absolute; left: 32px; top: 16px;
    font: italic 800 50px/1.08 "Barlow Condensed", sans-serif;
    color: var(--ink); text-transform: uppercase; letter-spacing: 0.5px;
    z-index: 2;
  }
  .subtitle {
    position: absolute; left: 32px; top: 134px;
    font: italic 800 32px/1 "Barlow Condensed", sans-serif;
    color: var(--club-blue); text-transform: uppercase;
    z-index: 2;
  }
  .cta {
    position: absolute; left: 32px; top: 239px;
    width: 192px; height: 34px; border-radius: 5px;
    background: var(--club-red); color: var(--paper);
    display: flex; align-items: center; justify-content: center;
    font: 700 16px/1 "Barlow Condensed", sans-serif; text-transform: uppercase;
    letter-spacing: 0.2px; z-index: 2;
  }
  .club-mark {
    position: absolute; left: 478px; top: 24px; width: 110px;
    display: flex; flex-direction: column; align-items: center; gap: 8px;
    z-index: 2;
  }
  .club-mark__name {
    font: 700 23px/1 "Barlow Condensed", sans-serif;
    color: var(--ink); text-transform: uppercase;
  }
  .club-mark__square { width: 84px; height: 84px; background: var(--club-blue); }
  .stripe { position: absolute; left: 0; width: 100%; background: var(--club-blue); }
  .stripe--1 { top: 319px; height: 5px; }
  .stripe--2 { top: 332px; height: 10px; }
  .stripe--3 { top: 353px; height: 16px; }
  .stripe--base { top: 380px; height: 125px; }
  .player-art {
    position: absolute; left: 312px; top: 152px; width: 262px; height: 298px;
    border-radius: 36px 36px 0 0;
    background: linear-gradient(160deg, var(--club-red) 0%, #b81a2c 55%, var(--player-dark) 100%);
    z-index: 1;
  }
  .promo {
    position: absolute; left: 32px; top: 406px;
    font: 700 15px/1.3 "Archivo", sans-serif; color: var(--navy);
    text-transform: uppercase; width: 270px; z-index: 2;
  }
  .footer {
    position: absolute; left: 32px; right: 45px; top: 469px;
    display: flex; align-items: center; gap: 8px;
    font: 600 13px/1 "Archivo", sans-serif; color: var(--paper);
    z-index: 2;
  }
  .footer__dot { width: 14px; height: 14px; border-radius: 50%; background: var(--paper); }
  .footer__rule { flex: 1; height: 2px; background: var(--paper); margin: 0 16px; }
</style>
</head>
<body>
  <main class="banner">
    <h1 class="title">Fête des lanternes<br>d'hiver</h1>
    <p class="subtitle">Grande Tombola</p>
    <a class="cta">Plus d'informations</a>

    <div class="club-mark">
      <span class="club-mark__name">FC Morlan</span>
      <span class="club-mark__square"></span>
    </div>

    <div class="stripe stripe--1"></div>
    <div class="stripe stripe--2"></div>
    <div class="stripe stripe--3"></div>
    <div class="stripe stripe--base"></div>

    <div class="player-art" role="img" aria-label="Illustration d'un footballeur en maillot rouge courant vers un ballon"></div>

    <p class="promo">Soutenez le FC Morlan et les restaurateurs locaux</p>

    <div class="footer">
      <span class="footer__dot"></span>
      <span class="footer__handle">@fcmorlan</span>
      <span class="footer__rule"></span>
      <span class="footer__url">www.fcmorlan.ch</span>
    </div>
  </main>
</body>
</html>
```